BRISK Form Renewals

12 Week Shape Renewal Scheme

website preview (it's not live yet) :

http://zorvatrainerpage.hostquill.example/preview/7qrwex.5mt3ba28ppdu8.a9416f2c84e329cb57139996de8c679f

colour palette:

RGB codes:

Yellow : R 242,G 206,B 130.
Pink : R 248, G 149,B 133
Dark Pink : R 190,G 108,B 106
Blue : R 38.G 69,B 97#4
Grey : R 78,G 110,B 130

Target Market(s)

Female’s wanting to lose weight, sculpt muscle who are lacking in confidence and feel overwhelmed and don’t know where to start in improving their fitness and lifestyle

Font styles to use
Sans Serif

Colors
fee3d4
ffffff

Requirements
Must have
• My specific colour palette - see above

```html
<!DOCTYPE html>
<html lang="en">
<head>
<meta charset="utf-8">
<title>BRISK Form Renewals – 12 Week Shape Renewal Scheme</title>
<link rel="stylesheet" href="https://fonts.googleapis.com/css2?family=Montserrat:wght@600;700&family=Roboto+Condensed:wght@700&family=Delius&display=swap">
<style>
  :root {
    --charcoal: #2a2a2a;
    --charcoal-light: #363535;
    --peach: #fee3d4;
    --white: #ffffff;
    --paper: #f2f2f4;
    --ink: #141414;
    --yellow: rgb(242,206,130);
    --pink: rgb(248,149,133);
    --dark-pink: rgb(190,108,106);
  }
  * { margin: 0; padding: 0; box-sizing: border-box; }
  html, body { width: 848px; height: 1200px; overflow: hidden; background: var(--charcoal); }
  .flyer {
    position: relative;
    width: 848px;
    height: 1200px;
    overflow: hidden;
    background: radial-gradient(ellipse at 30% 20%, var(--charcoal-light), var(--charcoal) 70%);
    font-family: "Montserrat", sans-serif;
  }
  .flyer__shapes { position: absolute; inset: 0; }
  .brand {
    position: absolute;
    top: 110px;
    left: 0;
    width: 100%;
    text-align: center;
    font-family: "Montserrat", sans-serif;
    font-weight: 700;
    font-size: 42px;
    letter-spacing: 6px;
    color: var(--pink);
  }
  .headline {
    position: absolute;
    right: 66px;
    top: 676px;
    font-family: "Montserrat", sans-serif;
    font-weight: 700;
    font-size: 138px;
    line-height: 1;
    letter-spacing: -4px;
    color: var(--peach);
  }
  .subhead {
    position: absolute;
    left: 314px;
    top: 810px;
    width: 476px;
    height: 44px;
    background: var(--peach);
    color: var(--ink);
    font-family: "Roboto Condensed", sans-serif;
    font-weight: 700;
    font-size: 40px;
    line-height: 44px;
    text-align: center;
    letter-spacing: -0.5px;
  }
  .scheme-label {
    position: absolute;
    left: 314px;
    width: 476px;
    top: 864px;
    text-align: center;
    font-family: "Montserrat", sans-serif;
    font-weight: 700;
    font-size: 28px;
    letter-spacing: 14px;
    color: var(--white);
  }
  .services {
    position: absolute;
    top: 920px;
    left: 278px;
    display: grid;
    grid-template-columns: 280px 270px;
    row-gap: 9px;
    list-style: none;
  }
  .services__item {
    display: flex;
    align-items: center;
    gap: 12px;
    font-family: "Delius", sans-serif;
    font-size: 26px;
    line-height: 26px;
    color: var(--peach);
  }
  .services__item::before {
    content: "";
    width: 18px;
    height: 18px;
    border-radius: 4px;
    background: var(--peach);
    flex: none;
  }
  .contact {
    position: absolute;
    left: 30px;
    top: 1090px;
    color: var(--ink);
    font-family: "Montserrat", sans-serif;
  }
  .contact__phone { font-size: 28px; font-weight: 700; line-height: 36px; }
  .contact__line { font-size: 18px; font-weight: 600; line-height: 27px; }
  .contact__sep { margin: 0 18px; }
</style>
</head>
<body>
<main class="flyer">
  <svg class="flyer__shapes" width="848" height="1200" viewBox="0 0 848 1200" aria-hidden="false">
    <defs>
      <linearGradient id="bandGradient" x1="0" y1="1" x2="1" y2="0">
        <stop offset="0" stop-color="rgb(190,108,106)"/>
        <stop offset="0.5" stop-color="rgb(248,149,133)"/>
        <stop offset="1" stop-color="rgb(242,206,130)"/>
      </linearGradient>
    </defs>
    <polygon class="photo-band" role="img"
      aria-label="Photo of a woman doing a kneeling leg-kick exercise over a tinted fitness collage"
      points="0,328 848,164 848,420 0,852" fill="url(#bandGradient)" opacity="0.92"/>
    <line class="accent-line" x1="0" y1="324" x2="408" y2="238" stroke="var(--peach)" stroke-width="2"/>
    <line class="accent-line" x1="424" y1="656" x2="848" y2="448" stroke="var(--peach)" stroke-width="2"/>
    <polygon class="contact-corner" points="0,986 688,1200 0,1200" fill="var(--paper)"/>
  </svg>

  <div class="brand">BRISK FORM RENEWALS</div>

  <h1 class="headline">12 WEEK</h1>
  <div class="subhead">SHAPE RENEWAL</div>
  <div class="scheme-label">SCHEME</div>

  <ul class="services">
    <li class="services__item">Weight Training</li>
    <li class="services__item">Diet Nutrition</li>
    <li class="services__item">Personal Training</li>
    <li class="services__item">Time Management</li>
    <li class="services__item">Yoga and Pilates</li>
    <li class="services__item">Martial Arts</li>
  </ul>

  <address class="contact">
    <div class="contact__phone">Call (303) 555 0148</div>
    <div class="contact__line">48 Harbor Lane, Portvale, PV 2389</div>
    <div class="contact__line">www.briskform.example<span class="contact__sep">|</span>info@briskform.example</div>
  </address>
</main>
</body>
</html>
```